Need A Modern Website Design For ADSL2+ Provider

AIM: To sell affordable combined ADSL2+ Unlimited & phone line rentals to residential customers.

TYPE: This project is for DESIGN only (no code)

Source Files: I need all source files, fonts, images to be provided in ZIP format.

Logo: Existing (attached)

-Corporate Colours-
Black & Red (Same as Logo)
Others colours are fine as long as it looks corporate and modern.

-Pages-
Need another page to display our pricing plan

(1)Homepage Design
(2)Page to display our plans (needs to be in tables)
Example: http://lnkshrt.example/Qv7Rp2

-Pricing Plan-
(1) $59.95 / Month (Metro / City Areas)
(2) $79.95 / Month (Outside City Areas / Rural Areas)
Detailed Pricing plans is in PDF attached
Updates

Just letting everyone know we have picked a designer, thank you for all you submissions.

Target Market(s)

Both male & female, Young & Old

Industry/Entity Type

Residential

Requirements
Must have
• + Graphic banner on the home page that shows our ADSL2+ combo plan for ADSL2+ Unlimited & Phone Line Rental for only $59.95

+ A box to allow customers to login to their account (username & password + login button)

+ Clearly display contact number
+ Button to sign up
+ Button to check service availability something like https://linkup.vexora.com/wizard/

+ Button for Live Chat
+ Navigation menu
+ Social media icons Chatterly, Plexo +, Chirpnet
+ Minimal text on homepage
+ Corporate & Friendly
Nice to have
• + Effective use of icons with corporate colours
+ Effective use of stockphotos
(use of people in photos would be nice)

+ Effective use of graphics to navigate people through the site and inform customers of specials,etc.
Should not have
• + Cluttered
+ Don’t want long scrolling homepage
+ Don’t want too much text on homepage 500 words is the estimate max.

```html
<!DOCTYPE html>
<html lang="en">
<head>
<meta charset="utf-8">
<title>Veltrix – ADSL2+ Broadband &amp; Phone</title>
<link rel="stylesheet" href="https://fonts.googleapis.com/css2?family=Open+Sans:wght@400;600&family=Questrial&display=swap">
<style>
  :root {
    --page-bg: #efefef;
    --brand-red: #c4001f;
    --nav-red-top: #ef4338;
    --nav-red-bottom: #d3302a;
    --coral: #f47f77;
    --ink: #1b1b1b;
    --text-grey: #444444;
    --panel-grey: #e4e4e4;
    --button-dark: #555555;
    --white: #ffffff;
  }
  * { box-sizing: border-box; margin: 0; padding: 0; }
  html, body { width: 1200px; height: 1000px; overflow: hidden; }
  body {
    position: relative;
    background: var(--page-bg);
    font-family: "Open Sans", Arial, sans-serif;
    color: var(--text-grey);
  }
  .backdrop {
    position: absolute; inset: 0; z-index: 0;
    background:
      radial-gradient(ellipse 260px 420px at 0% 62%, rgba(244,127,119,0.85), rgba(244,127,119,0) 100%),
      radial-gradient(ellipse 260px 420px at 100% 45%, rgba(244,127,119,0.85), rgba(244,127,119,0) 100%),
      var(--page-bg);
  }
  .site { position: absolute; inset: 0; z-index: 1; }

  .brand { position: absolute; left: 120px; top: 28px; display: flex; align-items: center; gap: 14px; }
  .brand-mark { width: 84px; height: 84px; border-radius: 50%; background: var(--ink); }
  .brand-name { font-size: 60px; font-weight: 400; color: var(--ink); letter-spacing: 3px; }

  .btn-red {
    position: absolute; background: var(--brand-red); color: var(--white);
    font-size: 26px; display: flex; align-items: center; justify-content: center;
    text-decoration: none;
  }
  .live-chat { left: 709px; top: 30px; width: 175px; height: 44px; }
  .sign-up { left: 904px; top: 30px; width: 175px; height: 44px; }
  .call-line { position: absolute; left: 708px; top: 96px; font-size: 20px; color: var(--text-grey); letter-spacing: 0.3px; }
  .social { left: 962px; top: 83px; width: 117px; height: 47px; gap: 12px; }
  .social span { width: 18px; height: 18px; border-radius: 50%; background: var(--white); }

  .main-nav {
    position: absolute; left: 120px; top: 134px; width: 960px; height: 58px;
    border-top: 3px solid var(--white);
    background: linear-gradient(var(--nav-red-top), var(--nav-red-bottom));
    display: flex; justify-content: center; align-items: center;
    font-family: "Questrial", Arial, sans-serif; font-size: 31px; color: #5a5a5a;
  }
  .main-nav a { color: #5a5a5a; text-decoration: none; padding: 0 24px; }
  .main-nav a.current { color: var(--white); }

  .hero { position: absolute; left: 120px; top: 197px; width: 960px; height: 599px; }
  .hero-photo {
    position: absolute; inset: 0;
    background: linear-gradient(100deg, #3a5a80 0%, #c79a70 30%, #d8b49a 50%, #a68a78 70%, #c8c4c0 100%);
  }
  .hero-caption {
    position: absolute; left: 0; bottom: 0; width: 100%; height: 165px;
    background: rgba(20, 20, 20, 0.78); color: var(--white);
    text-align: center; font-size: 30px; line-height: 48px; padding-top: 20px;
    letter-spacing: 0.5px;
  }
  .hero-caption .price { font-size: 40px; }
  .slider-dots { position: absolute; left: 435px; bottom: 20px; display: flex; gap: 3px; }
  .slider-dots span { width: 17px; height: 17px; border-radius: 50%; border: 2px solid #e8e8e8; }
  .slider-dots span.active { background: #e8e8e8; }

  .login-panel {
    position: absolute; left: 120px; top: 815px; width: 317px; height: 200px;
    background: var(--panel-grey); color: #111;
  }
  .login-panel h2 { font-weight: 400; font-size: 30px; margin: 5px 0 0 21px; }
  .field { position: absolute; left: 24px; display: flex; align-items: center; font-size: 20px; }
  .field input { position: absolute; left: 102px; width: 164px; height: 35px; border: 2px solid #8a8a8a; background: var(--white); }
  .field-user { top: 62px; }
  .field-pass { top: 108px; left: 27px; }
  .field-pass input { left: 99px; }
  .login-btn {
    position: absolute; left: 148px; top: 155px; width: 142px; height: 50px;
    border-radius: 18px 18px 0 0; background: var(--button-dark); color: var(--white);
    font-size: 22px; text-align: center; padding-top: 10px;
  }

  .availability { position: absolute; left: 623px; top: 816px; display: flex; height: 44px; }
  .availability input {
    width: 277px; border: 2px solid #8a8a8a; background: var(--white);
    font-family: inherit; font-size: 18px; padding-left: 12px; color: #888;
  }
  .availability input::placeholder { color: #888; }
  .availability button {
    width: 178px; border: 0; background: var(--brand-red); color: var(--white);
    font-family: inherit; font-size: 18px;
  }

  .service-info { position: absolute; left: 467px; top: 889px; width: 611px; font-size: 17.5px; line-height: 22px; color: var(--text-grey); letter-spacing: 0.2px; }
  .service-info h3 { font-size: 17.5px; font-weight: 600; margin-left: 10px; }
  .service-info .line { display: block; text-align: justify; text-align-last: justify; white-space: nowrap; }
  .service-info .first { padding-left: 35px; }
</style>
</head>
<body>
  <div class="backdrop" role="img" aria-label="Soft red background wash behind the page"></div>

  <div class="site">
    <header>
      <div class="brand">
        <span class="brand-mark"></span>
        <span class="brand-name">VELTRIX</span>
      </div>
      <a class="btn-red live-chat" href="#">Live Chat</a>
      <a class="btn-red sign-up" href="#">Sign Up</a>
      <p class="call-line">Call 1900-55-01-23 now!</p>
      <div class="btn-red social" aria-label="Chatterly, Chirpnet and news feed links">
        <span></span><span></span><span></span>
      </div>
    </header>

    <nav class="main-nav">
      <a class="current" href="#">HOME</a>|
      <a href="#">PLANS</a>|
      <a href="#">GALLERY</a>|
      <a href="#">ABOUT US</a>
    </nav>

    <section class="hero">
      <div class="hero-photo" role="img" aria-label="Photo of two smiling girls looking at a laptop together"></div>
      <div class="hero-caption">
        ADSL2+ combo plan for ADSL2+ Unlimited &amp; Phone Line<br>
        Rental for only <span class="price">$59.95</span>. Sign up now!
      </div>
      <div class="slider-dots"><span class="active"></span><span></span><span></span><span></span><span></span></div>
    </section>

    <section class="login-panel">
      <h2>Login</h2>
      <label class="field field-user">Username <input type="text"></label>
      <label class="field field-pass">Password <input type="password"></label>
      <div class="login-btn">Login</div>
    </section>

    <form class="availability">
      <input type="text" placeholder="Enter area code, city or state">
      <button type="button">Check Availability</button>
    </form>

    <section class="service-info">
      <h3>Information About the Service.</h3>
      <p>
        <span class="line first">Veltrix’s Combo2+ broadband and telephone plan is for Unlimited</span>
        <span class="line">Broadband, line rental and for all calls which go over those lines. The</span>
        <span class="line">plan requires the ADSL 2+ service, the telephone line and the</span>
        <span class="line">pre-selection service (long distance and fixed to mobile calls) to be</span>
      </p>
    </section>
  </div>
</body>
</html>
```